Redgate Business Card Design

We are a new small business specialising in under ground cable jointing and excavation works in NSW Australia.
Design I'm looking for is incorporating the Australian flag & excavator with out being to cheesy.
Maybe a faded washed out flag to help with overload of colour? & so its not the main focus.
Very open to creative out of the box designs!

Target Market(s)

Building & Construction

Industry/Entity Type

Construction

Contact Information for Business Card

Redgate Cable Jointing & Excavations
Colin Barwick

Ph: 0412 938 560
E: colin.barwick@tellnet.example

Reverse Side
Services we offer:
High Voltage & Low Voltage Cable Jointing
Polymeric & paperlead jointing & terminations
Trenching & Auger Drilling 150 - 600mm
Site preparation / leveling / clearing
Driveway / Footpath / Turf Prep
Rubbish Removal
Tree & Stump removal
Footings & Post holes
Drainage
Service Installs
Gravels & Sands available
Any general Earth moving needs
Reliable Free Quotes
Fully Insured

Font styles to use
Serif
Script

Requirements
Nice to have
• small excavator (See uploaded picture)

```html
<!DOCTYPE html>
<html lang="en">
<head>
<meta charset="utf-8">
<title>Redgate Business Card Design</title>
<link href="https://fonts.googleapis.com/css2?family=Oswald:wght@600&family=Roboto:wght@300;400;500&display=swap" rel="stylesheet">
<style>
  :root {
    --stage: #6b6b6b;
    --paper: #fbfbfc;
    --navy: #243378;
    --navy-deep: #1d2a66;
    --white: #ffffff;
    --wash: #e9ebf1;
    --wash-warm: #f6ebe6;
  }
  * { box-sizing: border-box; margin: 0; padding: 0; }
  html, body { width: 1200px; height: 1023px; overflow: hidden; }
  body {
    background: var(--stage);
    display: flex;
    align-items: center;
    justify-content: center;
    gap: 48px;
    font-family: "Roboto", sans-serif;
  }
  .card {
    width: 540px;
    height: 330px;
    position: relative;
    overflow: hidden;
    box-shadow: 0 10px 30px rgba(0,0,0,.35);
  }

  /* Front */
  .card-front { background: var(--paper); color: var(--navy); }
  .flag-wash {
    position: absolute; inset: 0;
    background:
      linear-gradient(120deg, var(--wash-warm) 0%, var(--wash) 28%, rgba(233,235,241,0) 70%),
      linear-gradient(0deg, var(--paper), var(--paper));
    opacity: .9;
  }
  .front-content {
    position: absolute; inset: 0;
    display: flex; flex-direction: column;
    align-items: center; justify-content: center;
    text-align: center;
  }
  .company { display: flex; flex-direction: column; align-items: flex-end; line-height: 1; }
  .company-name {
    font-family: "Oswald", sans-serif; font-weight: 600;
    font-size: 36px; letter-spacing: .5px; color: var(--navy);
  }
  .company-sub { font-weight: 300; font-size: 24px; letter-spacing: 1px; margin-top: 2px; }
  .mark {
    width: 34px; height: 34px; background: var(--navy);
    margin: 18px 0 14px;
  }
  .person {
    font-family: "Oswald", sans-serif; font-weight: 600;
    font-size: 24px; letter-spacing: .5px;
  }
  .contact {
    margin-top: 10px; font-weight: 400; font-size: 13px; letter-spacing: .5px;
    display: flex; gap: 14px;
  }

  /* Back */
  .card-back { background: var(--navy); color: var(--white); }
  .services {
    position: absolute; left: 60px; top: 32px; right: 30px;
    list-style: none;
    border-left: 3px solid var(--white);
    padding-left: 18px;
  }
  .service { font-size: 14.5px; line-height: 1.42; font-weight: 300; letter-spacing: .4px; }
  .service--caps { text-transform: uppercase; font-size: 13px; }
  .service--strong { font-weight: 500; }
</style>
</head>
<body>
  <section class="card card-front">
    <div class="flag-wash" role="img" aria-label="Faded, washed-out Australian flag in the background"></div>
    <div class="front-content">
      <div class="company">
        <span class="company-name">Redgate Cable</span>
        <span class="company-sub">Jointing &amp; Excavations</span>
      </div>
      <div class="mark"></div>
      <div class="person">Colin Barwick</div>
      <div class="contact">
        <span>0412 938 560</span>
        <span>colin.barwick@tellnet.example</span>
      </div>
    </div>
  </section>

  <section class="card card-back">
    <ul class="services">
      <li class="service">High Voltage &amp; Low Voltage Cable Jointing</li>
      <li class="service">Polymeric &amp; Paperlead Jointing &amp; Terminations</li>
      <li class="service service--strong">Trenching &amp; Auger Drilling 150 - 600mm</li>
      <li class="service">Site Preparation / Leveling / Clearing</li>
      <li class="service">Driveway / Footpath / Turf Prep</li>
      <li class="service service--caps">Rubbish Removal</li>
      <li class="service service--caps service--strong">Tree &amp; Stump Removal</li>
      <li class="service service--caps service--strong">Footings &amp; Post Holes</li>
      <li class="service">Drainage</li>
      <li class="service service--caps">Service Installs</li>
      <li class="service">Gravels &amp; Sands Available</li>
      <li class="service service--strong">Any General Earth Moving Needs</li>
      <li class="service">Reliable Free Quotes</li>
      <li class="service service--strong">Fully Insured</li>
    </ul>
  </section>
</body>
</html>
```